Bring me business with this creative business card

Design my new business card. I am looking for something different with an impact. People will take a look at this card & they will 1- see how different & creative I am, 2-understand what I do 3- Call me to meet me!

I make videos with a message, testimonials. I am dynamic, fun, creative & human. My new website is in construction but in the meantime you can check this old one: brightpath.ca & another one Fernquill.com & fernquill facebook page.
I make videos. sometimes with a cameraman, sometimes with my phone. As an ex Public Relations agent, the message is the most important thing for me. I want to make my clients shine! When they start with me they often remind me of a lamb, when I finish coaching them they are powerful like LIONS! That's why I need a powerful business card!

Target Market(s)

Entrepreneurs, solo entrepreneurs, small & medium companies & start ups. People i will meet while networking. People that need videos on their website & social Networks to get attention, to be visible. men & women. From 35 to 49 years old.
I am an ex Public relations agent. I used to send clients in traditional medias, now with videos they have more chances to be seen on google the new media. I do videos of the president, his team, his loyal clients saying how great the company is & expert videos like series so people can be seen for example every 1 st of every month with a short 2 minute video. Also with my 20 years in marketing & communications I can coach & give tips to anybody who needs it.
Target: anybody who would like my old website brightpath.ca & I also have another website but it will be off line soon: fernquill.com could give you ideas.

Industry/Entity Type

Communications

Contact Information for Business Card

I am in Montreal,So the business cards have to be the usual size like we have in Montreal: 9 cm x 5 cm
Details:My text: Corinne Vautrin Communication coach/Chief Lion. "Creating Videos as unique as you" off: 514-555-0147 cell: 514-555-0183. fernquill.com
corinne@fernquill.com logo facebook, youtube, instagram

Colors
f37122

Requirements
Must have
• Dynamic, happy. Orange. Be creative in the look but NOT the shape of the card. Easy to read. Big enough to read.
Should not have
• No funny shapes: no round, no square, just the usual. I love creative but NOT on shape.

```html
<!DOCTYPE html>
<html lang="en">
<head>
<meta charset="utf-8">
<title>Fernquill business card</title>
<link rel="stylesheet" href="https://fonts.googleapis.com/css2?family=Crimson+Pro:wght@500;600&family=Roboto+Condensed:wght@400;700&family=Roboto+Slab:wght@700&display=swap">
<style>
  :root {
    --backdrop: #a3381b;
    --brand-orange: #f37122;
    --deep-orange: #e8551f;
    --warm-yellow: #fbb51f;
    --bright-yellow: #ffd21a;
    --ink-grey: #6d6d6d;
    --paper: #ffffff;
  }
  html, body {
    margin: 0;
    width: 1200px;
    height: 900px;
    overflow: hidden;
    background: var(--backdrop);
  }
  .canvas {
    width: 1200px;
    height: 900px;
    display: flex;
    flex-direction: column;
    align-items: center;
    justify-content: center;
    gap: 40px;
  }
  .card {
    position: relative;
    width: 720px;
    height: 400px;
    border-radius: 26px;
    overflow: hidden;
    box-shadow: 0 10px 26px rgba(60, 12, 0, 0.35);
  }

  /* Back of card */
  .card--back { background: var(--brand-orange); }
  .lion-artwork {
    position: absolute;
    left: 0;
    bottom: 0;
    width: 330px;
    height: 340px;
    border-top-right-radius: 48% 40%;
    background:
      radial-gradient(circle at 55% 55%, var(--bright-yellow) 0%, var(--warm-yellow) 30%, transparent 62%),
      linear-gradient(135deg, var(--deep-orange), var(--warm-yellow) 55%, var(--deep-orange));
  }
  .tagline {
    position: absolute;
    left: 400px;
    top: 46px;
    margin: 0;
    font-family: "Crimson Pro", serif;
    font-weight: 600;
    font-size: 46px;
    line-height: 40px;
    letter-spacing: 2px;
    text-transform: uppercase;
    color: var(--paper);
  }
  .card--back .website {
    position: absolute;
    left: 360px;
    top: 262px;
    font-family: "Roboto Slab", serif;
    font-weight: 700;
    font-size: 21px;
    color: var(--paper);
  }

  /* Front of card */
  .card--front { background: var(--paper); }
  .brand {
    position: absolute;
    left: 44px;
    top: 46px;
    margin: 0;
    font-family: "Crimson Pro", serif;
    font-weight: 600;
    font-size: 66px;
    line-height: 60px;
    letter-spacing: 3px;
    color: var(--brand-orange);
  }
  .brand-dot {
    position: absolute;
    right: 58px;
    top: 34px;
    width: 130px;
    height: 130px;
    border-radius: 50%;
    background: var(--brand-orange);
  }
  .contact {
    position: absolute;
    left: 44px;
    top: 160px;
    font-family: "Roboto Condensed", sans-serif;
  }
  .contact__name {
    margin: 0;
    font-weight: 700;
    font-size: 28px;
    letter-spacing: 1px;
    text-transform: uppercase;
    color: var(--deep-orange);
  }
  .contact__role {
    margin: 2px 0 12px;
    font-size: 14px;
    letter-spacing: 1px;
    text-transform: uppercase;
    color: var(--ink-grey);
  }
  .contact__list {
    list-style: none;
    margin: 0;
    padding: 0;
  }
  .contact__item {
    display: flex;
    align-items: center;
    gap: 10px;
    font-size: 17px;
    line-height: 27px;
    color: var(--ink-grey);
    letter-spacing: 0.5px;
  }
  .contact__icon { width: 16px; height: 16px; }
  .social {
    display: flex;
    gap: 10px;
    margin-top: 10px;
  }
  .social__chip {
    width: 22px;
    height: 22px;
    border-radius: 4px;
    background: var(--brand-orange);
  }
  .card--front .website {
    position: absolute;
    left: 44px;
    bottom: 28px;
    font-family: "Roboto Slab", serif;
    font-weight: 700;
    font-size: 22px;
    color: var(--brand-orange);
  }
</style>
</head>
<body>
<main class="canvas">

  <section class="card card--back">
    <div class="lion-artwork" role="img" aria-label="Low-poly geometric lion head illustration in orange and yellow"></div>
    <h2 class="tagline">Creating<br>videos as<br>unique<br>as you</h2>
    <span class="website">www.fernquill.com</span>
  </section>

  <section class="card card--front">
    <h1 class="brand">FERNQUILL</h1>
    <div class="brand-dot"></div>

    <div class="contact">
      <h2 class="contact__name">Corinne Vautrin</h2>
      <p class="contact__role">Communication coach / Chief Lion</p>
      <ul class="contact__list">
        <li class="contact__item">
          <svg class="contact__icon" viewBox="0 0 16 16"><rect x="4" y="1" width="8" height="14" rx="1.5" fill="none" stroke="#f37122" stroke-width="1.8"/></svg>
          514-555-0183
        </li>
        <li class="contact__item">
          <svg class="contact__icon" viewBox="0 0 16 16"><path d="M4 1.5 L6.5 5 L5 6.8 Q6.8 10 9.2 11 L11 9.5 L14.5 12 L12.5 14.5 Q5 13 1.5 3.5 Z" fill="#f37122"/></svg>
          514-555-0147
        </li>
        <li class="contact__item">
          <svg class="contact__icon" viewBox="0 0 16 16"><rect x="1.5" y="3" width="13" height="10" rx="1" fill="none" stroke="#f37122" stroke-width="1.6"/><path d="M2 4 L8 9 L14 4" fill="none" stroke="#f37122" stroke-width="1.6"/></svg>
          corinne@fernquill.com
        </li>
      </ul>
      <div class="social" aria-label="Social profiles">
        <span class="social__chip"></span>
        <span class="social__chip"></span>
        <span class="social__chip"></span>
      </div>
    </div>

    <span class="website">www.fernquill.com</span>
  </section>

</main>
</body>
</html>
```